Luxury In Home Massages by five star therapist

My name is Tessa Coraline Whitby. I am a female massage therapist with many years of experience working in the luxury resort spa, in Holistic Wellness Centers and in providing the finest in- home visit massages. I am passionate about providing massages that enhance the mind/body well being of my client . I have clients who have been with me for years. My background includes owning my own Wellness Spa, specializing in prenatal, post partum massage, relaxing and rejuvenating massages (Deep Tissue, Myofascial Release, Connective Sculpting etc.) for both men and women. I am also a clinical aromatherapist and often incorporate aromatherapy in order to help with insomnia, stress, anxiety and stress that a busy lifestyle creates. I custom blend my essential oils for the needs of the client. Should one prefer scentless lotion, I use a luxury line from Valorine. I am currently open seeking to taking a few new clients in the evenings and on Sundays.I have excellent home visit references from residents of the Strands in Dana Point, Llido Isle, Nellie Gail, Newport Beach, Laguna BeachI want a very classy and elegant card with a feminine feel. Not just the same stock massage pictures I always see....This card MUST set me apart and appeal to the discerning/wealthy client

Target Market(s)

High end professionals/ homemakers/pregnant moms/

Industry/Entity Type

Health And Wellness

Font styles to use
Decorative
Script

Requirements
Must have
• A strikingly beautiful design with words connotating expertise and class.
Should not have
• a square, male look or the blah same old stock photography person on the massage table

```html
<!DOCTYPE html>
<html lang="en">
<head>
<meta charset="utf-8">
<title>Tessa Coraline Whitby – In Home Massage Postcard</title>
<link href="https://fonts.googleapis.com/css2?family=Lato:ital,wght@0,400;0,700;1,400;1,700;1,900&family=Marcellus&display=swap" rel="stylesheet">
<style>
  :root{
    --pink:#d8328f;
    --pink-deep:#c2267e;
    --charcoal:#2c2c2c;
    --blue:#3b69b6;
    --ring:#cfcfcf;
    --white:#ffffff;
    --text-dark:#333333;
    --stage:#ebe7e3;
  }
  *{margin:0;padding:0;box-sizing:border-box}
  html,body{width:825px;height:1200px;overflow:hidden}
  body{background:var(--stage);position:relative;font-family:"Lato",Arial,sans-serif}
  .card{position:absolute;left:92px;width:640px;height:415px;background:var(--white);overflow:hidden;box-shadow:0 3px 10px rgba(0,0,0,.25)}
  .card--front{top:152px}
  .card--back{top:612px;height:413px}
  .card-shapes{position:absolute;inset:0}
  .services-title{position:absolute;right:24px;top:20px;color:var(--white);font:italic 700 38px/40px "Lato",Arial,sans-serif;text-align:right}
  .services-list{position:absolute;right:12px;top:152px;list-style:none;text-align:right;font-size:11.5px;line-height:14px;color:var(--text-dark)}
  .services-list li{padding-right:14px;position:relative}
  .services-list .bullet::after{content:"";position:absolute;right:0;top:4px;width:7px;height:7px;border-radius:50%;background:var(--pink)}
  .therapist-name{position:absolute;left:18px;top:258px;color:var(--white);font:400 23px/1 "Marcellus",Georgia,serif;letter-spacing:.4px;white-space:nowrap}
  .therapist-bio{position:absolute;left:18px;top:299px;width:375px;color:#e6e6e6;font:italic 400 10.4px/14.2px "Lato",Arial,sans-serif;white-space:nowrap}
  .availability{position:absolute;left:27px;top:20px;color:var(--white);font:italic 700 20px/26.5px "Lato",Arial,sans-serif;white-space:nowrap}
  .references{position:absolute;left:27px;top:142px;color:#ececec;font:italic 400 12.4px/16.2px "Lato",Arial,sans-serif;white-space:nowrap}
  .call-pill{position:absolute;left:-4px;top:224px;width:225px;height:38px;border:3px solid var(--pink);border-radius:0 19px 19px 0;background:var(--white);padding-left:26px;color:var(--blue);font:italic 700 19.5px/32px "Lato",Arial,sans-serif;white-space:nowrap}
  .stamp-box{position:absolute;left:565px;top:24px;width:52px;height:50px;background:#e2e2e2}
</style>
</head>
<body>

<section class="card card--front">
  <svg class="card-shapes" width="640" height="415" viewBox="0 0 640 415">
    <defs>
      <linearGradient id="hotStoneTones" x1="0" y1="0" x2="1" y2="0.6">
        <stop offset="0" stop-color="#f6ece4"/><stop offset=".35" stop-color="#eccbb4"/><stop offset=".7" stop-color="#d9a789"/><stop offset="1" stop-color="#f2e6dc"/>
      </linearGradient>
      <radialGradient id="hotStoneGlow" cx=".3" cy=".45" r=".55">
        <stop offset="0" stop-color="#f3c9b4" stop-opacity=".9"/><stop offset="1" stop-color="#f3c9b4" stop-opacity="0"/>
      </radialGradient>
      <radialGradient id="roseAccent" cx="0" cy=".75" r=".22">
        <stop offset="0" stop-color="#b0162c" stop-opacity=".85"/><stop offset="1" stop-color="#b0162c" stop-opacity="0"/>
      </radialGradient>
      <linearGradient id="stoneShade" x1="0" y1="0" x2="0" y2="1">
        <stop offset="0" stop-color="#3a2a24" stop-opacity="0"/><stop offset=".8" stop-color="#6b4535" stop-opacity="0"/><stop offset="1" stop-color="#5a362a" stop-opacity=".45"/>
      </linearGradient>
      <radialGradient id="portraitGlow" cx=".5" cy=".55" r=".5">
        <stop offset="0" stop-color="#f6dccf"/><stop offset=".55" stop-color="#ecc0ad" stop-opacity=".85"/><stop offset="1" stop-color="#d8328f" stop-opacity="0"/>
      </radialGradient>
      <linearGradient id="darkPanel" x1="0" y1="0" x2="0" y2="1">
        <stop offset="0" stop-color="#4d4d4d"/><stop offset="1" stop-color="#222"/>
      </linearGradient>
      <radialGradient id="darkSheen" cx=".45" cy=".25" r=".6">
        <stop offset="0" stop-color="#777" stop-opacity=".35"/><stop offset="1" stop-color="#777" stop-opacity="0"/>
      </radialGradient>
      <linearGradient id="pinkPanel" x1="0" y1="0" x2="0" y2="1">
        <stop offset="0" stop-color="#e04ba0"/><stop offset="1" stop-color="#c9287f"/>
      </linearGradient>
      <radialGradient id="stillLife" cx=".5" cy=".55" r=".55">
        <stop offset="0" stop-color="#fff6e2"/><stop offset=".6" stop-color="#f4dfb0"/><stop offset="1" stop-color="#e3b96a"/>
      </radialGradient>
      <radialGradient id="smallPortrait" cx=".5" cy=".45" r=".55">
        <stop offset="0" stop-color="#f7e3da"/><stop offset="1" stop-color="#d9ad9b"/>
      </radialGradient>
    </defs>
    <g role="img" aria-label="Woman relaxing during a hot stone massage">
      <rect x="0" y="0" width="440" height="218" fill="url(#hotStoneTones)"/>
      <rect x="0" y="0" width="440" height="218" fill="url(#hotStoneGlow)"/>
      <rect x="0" y="0" width="440" height="218" fill="url(#roseAccent)"/>
      <rect x="0" y="0" width="440" height="218" fill="url(#stoneShade)"/>
    </g>
    <path d="M412 0 H640 V126 H458 Q430 70 412 0 Z" fill="url(#pinkPanel)"/>
    <path d="M408 0 Q428 72 456 126 H640" fill="none" stroke="#3a3a3a" stroke-width="4"/>
    <rect x="0" y="218" width="430" height="14" fill="var(--pink)"/>
    <path d="M0 232 H404 Q392 310 418 382 H0 Z" fill="url(#darkPanel)"/>
    <path d="M0 232 H404 Q392 310 418 382 H0 Z" fill="url(#darkSheen)"/>
    <path d="M410 240 H640 V382 H424 Q400 310 410 240 Z" fill="url(#pinkPanel)"/>
    <path d="M410 240 Q400 310 424 382" fill="none" stroke="var(--white)" stroke-width="4"/>
    <rect role="img" aria-label="Portrait of a woman holding a lily" x="450" y="240" width="170" height="142" fill="url(#portraitGlow)"/>
    <circle cx="398" cy="177" r="66" fill="var(--ring)"/>
    <circle cx="398" cy="177" r="58" fill="var(--white)" stroke="var(--blue)" stroke-width="3"/>
    <circle role="img" aria-label="Spa still life with candles, honey and daisies" cx="398" cy="177" r="53" fill="url(#stillLife)"/>
    <circle cx="423" cy="280" r="45" fill="var(--ring)"/>
    <circle cx="423" cy="280" r="38" fill="var(--white)" stroke="var(--blue)" stroke-width="3"/>
    <circle role="img" aria-label="Close-up of a woman with a white flower" cx="423" cy="280" r="34" fill="url(#smallPortrait)"/>
    <rect x="0" y="382" width="640" height="4" fill="var(--white)"/>
    <rect x="0" y="386" width="640" height="29" fill="var(--blue)"/>
  </svg>

  <h2 class="services-title">Services<br>includes</h2>
  <ul class="services-list">
    <li class="bullet">Wellness Spa</li>
    <li>specializing in prenatal</li>
    <li class="bullet">Post partum massage</li>
    <li class="bullet">Relaxing &amp; rejuvenating</li>
    <li>massages</li>
  </ul>

  <h1 class="therapist-name">Tessa Coraline Whitby</h1>
  <p class="therapist-bio">I am a female massage therapist with many years of experience working in<br>the luxury resort spa, in Holistic Wellness Centers and in providing the finest<br>in- home visit massages. I am passionate about providing massages that<br>enhance the mind/body well being of my client .</p>
</section>

<section class="card card--back">
  <svg class="card-shapes" width="640" height="413" viewBox="0 0 640 413">
    <defs>
      <linearGradient id="darkPanelBack" x1="0" y1="0" x2="0" y2="1">
        <stop offset="0" stop-color="#474747"/><stop offset="1" stop-color="#222"/>
      </linearGradient>
      <radialGradient id="darkSheenBack" cx=".5" cy=".35" r=".6">
        <stop offset="0" stop-color="#777" stop-opacity=".3"/><stop offset="1" stop-color="#777" stop-opacity="0"/>
      </radialGradient>
      <linearGradient id="stoneStrip" x1="0" y1="0" x2="1" y2="0">
        <stop offset="0" stop-color="#a9cb5a"/><stop offset=".2" stop-color="#e9d6bd"/><stop offset=".7" stop-color="#e4bfa2"/><stop offset="1" stop-color="#8fb84a"/>
      </linearGradient>
      <linearGradient id="stripShade" x1="0" y1="0" x2="0" y2="1">
        <stop offset="0" stop-color="#fff" stop-opacity=".25"/><stop offset=".6" stop-color="#fff" stop-opacity="0"/><stop offset="1" stop-color="#5a3a2a" stop-opacity=".3"/>
      </linearGradient>
    </defs>
    <path d="M0 0 H352 Q325 60 305 120 H0 Z" fill="var(--pink)"/>
    <path d="M0 128 H302 Q283 190 282 250 Q282 330 300 380 H0 Z" fill="url(#darkPanelBack)"/>
    <path d="M0 128 H302 Q283 190 282 250 Q282 330 300 380 H0 Z" fill="url(#darkSheenBack)"/>
    <path d="M368 0 Q300 140 296 250 Q294 330 314 385" fill="none" stroke="var(--blue)" stroke-width="7"/>
    <rect x="28" y="283" width="230" height="78" fill="var(--white)"/>
    <g role="img" aria-label="Hot stones along a relaxed back">
      <rect x="32" y="287" width="222" height="70" fill="url(#stoneStrip)"/>
      <rect x="32" y="287" width="222" height="70" fill="url(#stripShade)"/>
    </g>
    <rect x="0" y="385" width="640" height="28" fill="var(--blue)"/>
  </svg>

  <h2 class="availability">Seeking to taking a few new<br>clients in the evenings and<br>on Sundays.</h2>
  <p class="references">I have excellent home visit references<br>from residents of the Strands in Dana<br>Point, Llido Isle, Nellie Gail, Newport<br>Beach, Laguna Beach</p>
  <div class="call-pill">Call: 555 204 318</div>
  <div class="stamp-box"></div>
</section>

</body>
</html>
```